Business Card Design Project

I need a business card designed from scratch. I have an existing logo that I can upload in Illustrator for modification or redesign.

The Company is called Rank Harbor http://rankharbor.com.au and we provide Search Engine Optimization services to Australian businesses. The current logo signifies an increase in visitors, profits etc...

There are no restrictions as to the redesign - colours, style etc are all open to change.

Cards will be full colour and one sided printed at http://www.printlorvex.com.au so check their requirements for file format and sizes etc.

I will expect all original files upon completion of project.

Target Market(s)

Any business with a web site looking to improve their search engine rankings

Industry/Entity Type

Business

Requirements
Must have
• I like modern, sleek designs. Clean, not fussy, uncluttered.

```html
<!DOCTYPE html>
<html lang="en">
<head>
<meta charset="utf-8">
<title>Rank Harbor – Business Card</title>
<link href="https://fonts.googleapis.com/css2?family=Open+Sans:wght@400;600;700&display=swap" rel="stylesheet">
<style>
  :root {
    --brand-blue: #1a72b9;
    --accent-yellow: #f5c518;
    --card-white: #ffffff;
    --ink: #3d3d3d;
    --backdrop: #e9e9e9;
  }
  * { margin: 0; padding: 0; box-sizing: border-box; }
  html, body {
    width: 1200px; height: 460px; overflow: hidden;
    background: var(--backdrop);
    font-family: "Open Sans", sans-serif;
  }
  .stage { position: relative; width: 1200px; height: 460px; }

  .card {
    position: absolute;
    width: 524px; height: 298px;
    border-radius: 16px;
    overflow: hidden;
    box-shadow: 0 4px 10px rgba(0,0,0,0.18);
  }
  .card--front { left: 35px; top: 70px; background: var(--card-white); }
  .card--back  { left: 604px; top: 75px; background: var(--brand-blue); }

  /* front */
  .brand {
    position: absolute; left: 42px; top: 58px;
    display: flex; align-items: center; gap: 12px;
  }
  .brand__dot {
    width: 22px; height: 22px; border-radius: 50%;
    background: var(--accent-yellow);
  }
  .brand__name {
    font-weight: 700; font-size: 36px; line-height: 1;
    color: var(--brand-blue); letter-spacing: -0.5px;
  }
  .name-band {
    position: absolute; left: 0; top: 165px;
    width: 100%; height: 28px;
    background: var(--brand-blue);
    color: #fff;
    padding-left: 22px;
    display: flex; align-items: center; gap: 5px;
  }
  .name-band__name { font-weight: 700; font-size: 16px; }
  .name-band__title { font-weight: 400; font-size: 12.5px; }
  .accent-disc {
    position: absolute; left: 400px; top: 128px;
    width: 66px; height: 66px; border-radius: 50%;
    background: var(--accent-yellow);
  }
  .contact {
    position: absolute; top: 238px;
    font-size: 12.5px; line-height: 19px; color: var(--ink);
  }
  .contact--address { left: 20px; }
  .contact--phones  { left: 190px; }
  .contact--online  { left: 295px; }
  .contact__row { display: flex; align-items: center; gap: 5px; white-space: nowrap; }
  .contact__icon { width: 10px; height: 10px; fill: var(--brand-blue); flex: none; }

  /* back */
  .back-brand {
    position: absolute; left: 0; top: 108px; width: 100%;
    text-align: center;
    font-weight: 700; font-size: 40px; color: #fff; letter-spacing: -0.5px;
  }
  .back-url {
    position: absolute; left: 0; top: 225px; width: 100%;
    text-align: center;
    font-size: 13px; color: #fff; letter-spacing: 1.2px;
  }
</style>
</head>
<body>
<main class="stage">

  <section class="card card--front" aria-label="Card front">
    <div class="brand">
      <span class="brand__dot"></span>
      <span class="brand__name">Rank Harbor</span>
    </div>

    <div class="name-band">
      <span class="name-band__name">Your Name</span>
      <span class="name-band__title">Title</span>
    </div>
    <span class="accent-disc"></span>

    <div class="contact contact--address">
      <p>00Floor Street, City Name</p>
      <p>State Name, Contry Name</p>
    </div>

    <div class="contact contact--phones">
      <p class="contact__row">
        <svg class="contact__icon" viewBox="0 0 10 10"><path d="M2 0.5 L4 2.5 L3 3.8 Q4.5 6 6.2 7 L7.5 6 L9.5 8 L8 9.6 Q3.5 9 0.4 2 Z"/></svg>
        098 765 4321
      </p>
      <p class="contact__row">
        <svg class="contact__icon" viewBox="0 0 10 10"><rect x="2.5" y="0" width="5" height="10" rx="1"/><rect x="3.4" y="1.2" width="3.2" height="5.8" fill="#fff"/></svg>
        098 765 4321
      </p>
    </div>

    <div class="contact contact--online">
      <p class="contact__row">
        <svg class="contact__icon" viewBox="0 0 10 10"><rect x="0" y="2" width="10" height="6.5" rx="0.8"/><path d="M0.5 2.5 L5 5.8 L9.5 2.5" stroke="#fff" stroke-width="0.9" fill="none"/></svg>
        enquiry@rankharbor.com.au
      </p>
      <p class="contact__row">
        <svg class="contact__icon" viewBox="0 0 10 10"><circle cx="5" cy="5" r="4.6"/></svg>
        www.rankharbor.com.au
      </p>
    </div>
  </section>

  <section class="card card--back" aria-label="Card back">
    <p class="back-brand">Rank Harbor</p>
    <p class="back-url">www.rankharbor.com.au</p>
  </section>

</main>
</body>
</html>
```